Corportate Power Point Template

We need a corporate PPT Design for our startup Big Data company.

Basically, our company will ingest, analyze and generate dynamic Dashboards with data consumed from different sources like Social Networks, Enterprise Legacy Systems such as e-Commerce, ERP, CRM and others.

Company is headquartered in Brazil, but will have a global presence.

Industry/Entity Type

It Company

```html
<!DOCTYPE html>
<html lang="en">
<head>
<meta charset="utf-8">
<title>Quantiva – Corporate Presentation Template</title>
<link href="https://fonts.googleapis.com/css2?family=Roboto+Slab:wght@400;700&family=Open+Sans:wght@300;400;600;700&display=swap" rel="stylesheet">
<style>
:root{
  --orange:#f15a22;
  --orange-soft:#f6a27f;
  --yellow:#f7b500;
  --gray:#5a5a5a;
  --text:#555;
  --light:#e9e9e9;
  --dark:#111;
  --page:#fff;
}
*{box-sizing:border-box;margin:0;padding:0}
html,body{width:1159px;height:1200px;overflow:hidden;background:var(--page);font-family:"Open Sans",sans-serif;color:var(--text)}
.sheet{position:relative;width:1159px;height:1200px}
.slide{position:absolute;width:341px;height:256px;background:#fff;overflow:hidden;box-shadow:0 1px 5px rgba(0,0,0,.35)}
.c1{left:38px}.c2{left:407px}.c3{left:778px}
.r1{top:50px}.r2{top:331px}.r3{top:613px}.r4{top:894px}
.slide-title{position:absolute;left:12px;top:5px;font-family:"Roboto Slab",serif;font-weight:700;font-size:14px;color:var(--orange)}
.slide-sub{position:absolute;left:13px;top:24px;font-size:8.5px;color:#777}
.badge{position:absolute;right:10px;top:5px;width:17px;height:17px;background:var(--orange);color:#fff;font-size:9px;display:flex;align-items:center;justify-content:center}
.footer{position:absolute;left:8px;right:10px;bottom:8px;height:12px;display:flex;align-items:center;gap:5px}
.brand{font-family:"Open Sans",sans-serif;font-weight:600;font-size:9.5px;color:var(--orange);display:flex;align-items:center;gap:3px;white-space:nowrap}
.brand i{display:inline-block;width:7px;height:7px;background:var(--orange)}
.footer .rule{flex:1;height:1px;background:#ccc}
.footer .nav{font-size:5px;color:#999;white-space:nowrap}
.footer .nav b{font-weight:400;color:var(--orange-soft);margin-right:8px}
.tile{position:absolute;right:0;bottom:0;width:150px;height:110px;background:linear-gradient(135deg,transparent 40%,#f2f2f2 100%)}
.body{font-size:5.2px;line-height:1.6;color:var(--text)}
.head-caps{font-size:10px;color:var(--orange);text-transform:uppercase}
.pic{background:var(--orange);display:flex;align-items:center;justify-content:center}
.cover-photo{position:absolute;inset:0;background:radial-gradient(circle at 40% 60%,#3f6f7d 0%,#1c3b48 40%,#0b1a22 80%)}
.cover-suit{position:absolute;left:120px;top:0;width:170px;height:256px;background:linear-gradient(90deg,#15181b,#26292c 50%,#15181b)}
.cover-logo{position:absolute;right:0;top:13px;width:182px;height:54px;background:#e6e6e6;display:flex;align-items:center;justify-content:center}
.cover-logo .brand{font-size:18px}
.cover-logo .brand i{width:14px;height:14px}
.cover-band{position:absolute;left:0;right:0;top:190px;height:50px;background:rgba(0,0,0,.85);padding:6px 10px}
.cover-band h1{font-family:"Roboto Slab",serif;font-size:16px;color:#fff;font-weight:400}
.cover-band p{font-size:10px;color:#ddd}
.thanks{background:var(--orange)}
.thanks h2{position:absolute;left:18px;top:146px;font-weight:300;font-size:22px;color:#fff;letter-spacing:.5px;line-height:26px}
.thanks .line{position:absolute;left:18px;top:174px;width:140px;height:1px;background:rgba(255,255,255,.6)}
.contact{position:absolute;left:26px;font-size:6px;line-height:8px;color:#fff;display:flex;align-items:center;gap:9px}
.social{position:absolute;left:22px;top:242px;display:flex;gap:8px}
.social span{width:8px;height:8px;background:#fff}
</style>
</head>
<body>
<div class="sheet">

<section class="slide c1 r1">
  <div class="cover-photo" role="img" aria-label="Businessman in a dark suit presenting sketched cloud and device icons on a teal background"></div>
  <div class="cover-suit" role="img" aria-label="Suit of the presenter"></div>
  <div class="cover-logo"><span class="brand"><i></i>Quantiva</span></div>
  <div class="cover-band"><h1>TITLE OF YOUR SLIDE</h1><p>Description here</p></div>
</section>

<section class="slide c2 r1">
  <div class="tile"></div>
  <div class="slide-title">About Us</div><div class="slide-sub">text for second title</div><div class="badge">2</div>
  <div class="head-caps" style="position:absolute;left:17px;top:67px">Lorem ipsum dolor sit amet</div>
  <p class="body" style="position:absolute;left:17px;top:85px;width:175px">Lorem ipsum dolor sit amet, consectetur adipiscing elit. Aliquam odio nulla, blandit eu suscipit ac, pulvinar in mauris. Mauris ac sodales ante. Donec congue lectus vel libero facilisis luctus. Lorem ipsum dolor sit amet, consectetur adipiscing elit. Aliquam odio nulla, blandit eu suscipit ac, pulvinar in mauris. Mauris ac sodales ante. Donec congue lectus vel libero facilisis luctus. Lorem ipsum dolor sit amet, consectetur adipiscing elit. Aliquam odio nulla, blandit eu suscipit ac, pulvinar in mauris. Mauris ac sodales ante. Donec congue lectus vel libero facilisis luctus.</p>
  <div class="pic" role="img" aria-label="Image placeholder" style="position:absolute;left:195px;top:64px;width:135px;height:146px">
    <svg width="80" height="60" viewBox="0 0 80 60"><rect x="2" y="4" width="46" height="36" rx="4" fill="none" stroke="#fff" stroke-width="3" transform="rotate(-12 25 22)"/><rect x="20" y="14" width="56" height="42" rx="4" fill="#fff"/><path d="M26 50 L42 30 L52 42 L58 36 L70 50Z" fill="var(--orange)"/><circle cx="62" cy="24" r="4" fill="var(--orange)"/></svg>
  </div>
  <div class="footer"><span class="brand"><i></i>Quantiva</span><span class="rule"></span><span class="nav"><b>Next</b>Previous</span></div>
</section>

<section class="slide c3 r1">
  <div class="tile"></div>
  <div role="img" aria-label="Colourful bokeh light photograph in blue, teal and amber" style="position:absolute;left:0;top:0;width:170px;height:256px;background:radial-gradient(circle at 30% 20%,#d9b436 0%,#6a8a3a 18%,transparent 35%),radial-gradient(circle at 70% 60%,#2d9be0 0%,#1557b0 30%,transparent 55%),linear-gradient(160deg,#0a2a6a,#02103a)"></div>
  <div class="badge">3</div>
  <div class="slide-title" style="left:184px;top:44px">Image &amp; Texts</div>
  <div class="slide-sub" style="left:184px;top:63px">text for second title</div>
  <p class="body" style="position:absolute;left:184px;top:85px;width:148px">Lorem ipsum dolor sit amet, consectetur adipiscing elit. Aliquam odio nulla, blandit eu suscipit ac, pulvinar in mauris. Mauris ac sodales ante. Donec congue lectus vel libero facilisis luctus. Lorem ipsum dolor sit amet, consectetur adipiscing elit. Aliquam odio nulla, blandit eu suscipit ac, pulvinar in mauris. Mauris ac sodales ante. Donec congue lectus vel libero facilisis luctus. Lorem ipsum dolor sit amet, consectetur adipiscing elit. Aliquam odio nulla, blandit eu suscipit ac, pulvinar in mauris. Mauris ac sodales ante. Donec congue lectus vel libero facilisis luctus. Lorem ipsum dolor sit amet, consectetur adipiscing elit. Aliquam odio nulla, blandit eu suscipit ac, pulvinar in mauris.</p>
</section>

<section class="slide c1 r2">
  <div class="tile"></div>
  <div class="slide-title">Left Column Style</div><div class="slide-sub">text for second title</div><div class="badge">4</div>
  <div style="position:absolute;left:72px;top:72px;font-size:12px;color:#bbb;font-family:Georgia,serif">“</div>
  <p class="body" style="position:absolute;left:28px;top:88px;width:98px;text-align:center;font-size:5.8px"><b>Lorem ipsum dolor sit amet,</b> consectetur adipiscing elit. Aliquam odio nulla, blandit eu suscipit ac, pulvinar in mauris. Mauris ac sodales ante. Donec congue lectus vel libero facilisis luctus.</p>
  <div style="position:absolute;left:72px;top:188px;font-size:12px;color:#bbb;font-family:Georgia,serif">”</div>
  <div style="position:absolute;left:136px;top:82px;width:1px;height:130px;background:#ddd"></div>
  <div class="head-caps" style="position:absolute;left:143px;top:62px">Lorem ipsum dolor sit amet</div>
  <div class="body" style="position:absolute;left:143px;top:85px;width:185px;display:grid;gap:9px">
    <p>Lorem ipsum dolor sit amet, consectetur adipiscing elit. Aliquam odio nulla, blandit eu suscipit ac, pulvinar in mauris. Mauris ac sodales ante. Donec congue lectus vel libero facilisis luctus.</p>
    <p>Lorem ipsum dolor sit amet, consectetur adipiscing elit. Aliquam odio nulla, blandit eu suscipit ac, pulvinar in mauris. Mauris ac sodales ante. Donec congue lectus vel libero facilisis luctus.</p>
    <p>Lorem ipsum dolor sit amet, consectetur adipiscing elit. Aliquam odio nulla, blandit eu suscipit ac, pulvinar in mauris. Mauris ac sodales ante. Donec congue lectus vel libero facilisis luctus.</p>
  </div>
  <div class="footer"><span class="brand"><i></i>Quantiva</span><span class="rule"></span><span class="nav"><b>Next</b>Previous</span></div>
</section>

<section class="slide c2 r2">
  <div class="tile"></div>
  <div class="slide-title">Iconic Style</div><div class="slide-sub">text for second title</div><div class="badge">5</div>
  <div style="position:absolute;left:30px;top:58px;width:290px;display:flex;justify-content:space-between">
    <div style="width:100px;text-align:center">
      <div class="pic" style="width:58px;height:58px;margin:0 auto"><svg width="28" height="24" viewBox="0 0 28 24" fill="none" stroke="#fff" stroke-width="2.2"><path d="M1 3h5l4 12h12l3-9H8"/><circle cx="11" cy="20" r="2" fill="#fff"/><circle cx="21" cy="20" r="2" fill="#fff"/></svg></div>
      <div style="font-size:7px;color:var(--orange);margin:9px 0 6px">Lorem ipsum</div>
      <p class="body">Lorem ipsum dolor sit amet, consectetur adipiscing elit. Aliquam odio nulla, blandit eu suscipit ac, pulvinar in mauris. Mauris ac sodales ante. Donec congue lectus vel libero facilisis luctus.</p>
    </div>
    <div style="width:100px;text-align:center">
      <div class="pic" style="width:58px;height:58px;margin:0 auto"><svg width="30" height="26" viewBox="0 0 30 26" fill="#fff"><circle cx="19" cy="5" r="4"/><rect x="13" y="11" width="12" height="12" rx="2"/><circle cx="7" cy="10" r="3"/><rect x="2" y="15" width="10" height="9" rx="2"/></svg></div>
      <div style="font-size:7px;color:var(--orange);margin:9px 0 6px">Lorem ipsum</div>
      <p class="body">Lorem ipsum dolor sit amet, consectetur adipiscing elit. Aliquam odio nulla, blandit eu suscipit ac, pulvinar in mauris. Mauris ac sodales ante. Donec congue lectus vel libero facilisis luctus.</p>
    </div>
    <div style="width:100px;text-align:center">
      <div class="pic" style="width:58px;height:58px;margin:0 auto"><svg width="30" height="30" viewBox="0 0 30 30" fill="none" stroke="#fff" stroke-width="2"><circle cx="15" cy="13" r="6" fill="#fff"/><path d="M12 21h6M13 24h4M15 1v3M3 13h3M24 13h3M6 5l2 2M24 5l-2 2"/></svg></div>
      <div style="font-size:7px;color:var(--orange);margin:9px 0 6px">Lorem ipsum</div>
      <p class="body">Lorem ipsum dolor sit amet, consectetur adipiscing elit. Aliquam odio nulla, blandit eu suscipit ac, pulvinar in mauris. Mauris ac sodales ante. Donec congue lectus vel libero facilisis luctus.</p>
    </div>
  </div>
  <div class="footer"><span class="brand"><i></i>Quantiva</span><span class="rule"></span><span class="nav"><b>Next</b>Previous</span></div>
</section>

<section class="slide c3 r2">
  <div class="tile"></div>
  <div class="slide-title">The Team</div><div class="slide-sub">text for second title</div><div class="badge">6</div>
  <div style="position:absolute;left:9px;top:42px;width:326px;height:178px;display:grid;grid-template-columns:repeat(4,1fr);gap:2px">
    <div style="background:var(--orange);display:flex;flex-direction:column">
      <div class="pic" role="img" aria-label="Team member photo placeholder" style="height:105px"><svg width="70" height="50" viewBox="0 0 80 60"><rect x="2" y="4" width="46" height="36" rx="4" fill="none" stroke="#fff" stroke-width="3" transform="rotate(-12 25 22)"/><rect x="20" y="14" width="56" height="42" rx="4" fill="#fff"/><path d="M26 50 L42 30 L52 42 L58 36 L70 50Z" fill="var(--orange)"/></svg></div>
      <div style="background:var(--orange-soft);color:#fff;font-size:6px;font-weight:700;padding:4px 2px">John Doe | Manager</div>
      <p class="body" style="color:#fff;padding:4px;font-size:4.6px">Lorem ipsum dolor sit amet, consectetur adipiscing elit. Aliquam odio nulla, blandit eu suscipit ac, pulvinar in mauris. Mauris ac sodales ante. Donec congue lectus vel libero facilisis luctus.</p>
    </div>
    <div style="background:var(--orange);display:flex;flex-direction:column">
      <div class="pic" role="img" aria-label="Team member photo placeholder" style="height:105px"><svg width="70" height="50" viewBox="0 0 80 60"><rect x="2" y="4" width="46" height="36" rx="4" fill="none" stroke="#fff" stroke-width="3" transform="rotate(-12 25 22)"/><rect x="20" y="14" width="56" height="42" rx="4" fill="#fff"/><path d="M26 50 L42 30 L52 42 L58 36 L70 50Z" fill="var(--orange)"/></svg></div>
      <div style="background:var(--orange-soft);color:#fff;font-size:6px;font-weight:700;padding:4px 2px">John Doe | Manager</div>
      <p class="body" style="color:#fff;padding:4px;font-size:4.6px">Lorem ipsum dolor sit amet, consectetur adipiscing elit. Aliquam odio nulla, blandit eu suscipit ac, pulvinar in mauris. Mauris ac sodales ante. Donec congue lectus vel libero facilisis luctus.</p>
    </div>
    <div style="background:var(--orange);display:flex;flex-direction:column">
      <div class="pic" role="img" aria-label="Team member photo placeholder" style="height:105px"><svg width="70" height="50" viewBox="0 0 80 60"><rect x="2" y="4" width="46" height="36" rx="4" fill="none" stroke="#fff" stroke-width="3" transform="rotate(-12 25 22)"/><rect x="20" y="14" width="56" height="42" rx="4" fill="#fff"/><path d="M26 50 L42 30 L52 42 L58 36 L70 50Z" fill="var(--orange)"/></svg></div>
      <div style="background:var(--orange-soft);color:#fff;font-size:6px;font-weight:700;padding:4px 2px">John Doe | Manager</div>
      <p class="body" style="color:#fff;padding:4px;font-size:4.6px">Lorem ipsum dolor sit amet, consectetur adipiscing elit. Aliquam odio nulla, blandit eu suscipit ac, pulvinar in mauris. Mauris ac sodales ante. Donec congue lectus vel libero facilisis luctus.</p>
    </div>
    <div style="background:var(--orange);display:flex;flex-direction:column">
      <div class="pic" role="img" aria-label="Team member photo placeholder" style="height:105px"><svg width="70" height="50" viewBox="0 0 80 60"><rect x="2" y="4" width="46" height="36" rx="4" fill="none" stroke="#fff" stroke-width="3" transform="rotate(-12 25 22)"/><rect x="20" y="14" width="56" height="42" rx="4" fill="#fff"/><path d="M26 50 L42 30 L52 42 L58 36 L70 50Z" fill="var(--orange)"/></svg></div>
      <div style="background:var(--orange-soft);color:#fff;font-size:6px;font-weight:700;padding:4px 2px">John Doe | Manager</div>
      <p class="body" style="color:#fff;padding:4px;font-size:4.6px">Lorem ipsum dolor sit amet, consectetur adipiscing elit. Aliquam odio nulla, blandit eu suscipit ac, pulvinar in mauris. Mauris ac sodales ante. Donec congue lectus vel libero facilisis luctus.</p>
    </div>
  </div>
  <div class="footer"><span class="brand"><i></i>Quantiva</span><span class="rule"></span><span class="nav"><b>Next</b>Previous</span></div>
</section>

<section class="slide c1 r3">
  <div class="tile"></div>
  <div class="slide-title">Team Member</div><div class="slide-sub">text for second title</div><div class="badge">7</div>
  <div class="pic" role="img" aria-label="Team member photo placeholder" style="position:absolute;left:10px;top:53px;width:88px;height:95px"><svg width="74" height="54" viewBox="0 0 80 60"><rect x="2" y="4" width="46" height="36" rx="4" fill="none" stroke="#fff" stroke-width="3" transform="rotate(-12 25 22)"/><rect x="20" y="14" width="56" height="42" rx="4" fill="#fff"/><path d="M26 50 L42 30 L52 42 L58 36 L70 50Z" fill="var(--orange)"/></svg></div>
  <div style="position:absolute;left:12px;top:158px;display:grid;gap:8px;font-size:7px;color:#777">
    <div style="display:flex;gap:6px;align-items:center"><span style="width:9px;height:9px;border-radius:50%;background:var(--orange)"></span>lorem ipsum</div>
    <div style="display:flex;gap:6px;align-items:center"><span style="width:9px;height:9px;border-radius:50%;background:var(--orange)"></span>lorem ipsum</div>
    <div style="display:flex;gap:6px;align-items:center"><span style="width:9px;height:9px;background:var(--orange)"></span>lorem ipsum</div>
  </div>
  <div class="head-caps" style="position:absolute;left:113px;top:55px">Lorem ipsum dolor sit amet</div>
  <div style="position:absolute;left:113px;top:69px;font-size:7.5px;color:#777">lorem ipsum dolor sit amet</div>
  <div class="body" style="position:absolute;left:113px;top:87px;width:215px;display:grid;gap:9px">
    <p>Lorem ipsum dolor sit amet, consectetur adipiscing elit. Aliquam odio nulla, blandit eu suscipit ac, pulvinar in mauris. Mauris ac sodales ante. Donec congue lectus vel libero facilisis luctus.</p>
    <p>Lorem ipsum dolor sit amet, consectetur adipiscing elit. Aliquam odio nulla, blandit eu suscipit ac, pulvinar in mauris. Mauris ac sodales ante. Donec congue lectus vel libero facilisis luctus.</p>
    <p>Lorem ipsum dolor sit amet, consectetur adipiscing elit. Aliquam odio nulla, blandit eu suscipit ac, pulvinar in mauris. Mauris ac sodales ante. Donec congue lectus vel libero facilisis luctus.</p>
  </div>
  <div class="footer"><span class="brand"><i></i>Quantiva</span><span class="rule"></span><span class="nav"><b>Next</b>Previous</span></div>
</section>

<section class="slide c2 r3">
  <div class="tile"></div>
  <div class="slide-title">Bulletins Style</div><div class="slide-sub">text for second title</div><div class="badge">8</div>
  <div class="body" style="position:absolute;left:27px;top:56px;width:290px;display:grid;gap:8px">
    <p style="position:relative"><span style="position:absolute;left:-8px;top:1px;width:5px;height:5px;border-radius:50%;background:var(--orange)"></span>Lorem ipsum dolor sit amet, consectetur adipiscing elit. Aliquam odio nulla, blandit eu suscipit ac, pulvinar in mauris. Mauris ac sodales ante. Donec congue lectus vel libero facilisis luctus.</p>
    <div style="padding-left:24px;display:grid;gap:4px;font-size:4.6px">
      <p>• Lorem ipsum dolor sit amet, consectetur adipiscing elit. Aliquam odio nulla, blandit eu suscipit ac, pulvinar in mauris. Mauris ac sodales ante. Donec congue lectus vel libero facilisis luctus.</p>
      <p>• Lorem ipsum dolor sit amet, consectetur adipiscing elit. Aliquam odio nulla, blandit eu suscipit ac, pulvinar in mauris. Mauris ac sodales ante. Donec congue lectus vel libero facilisis luctus.</p>
    </div>
    <p style="position:relative;margin-top:6px"><span style="position:absolute;left:-8px;top:1px;width:5px;height:5px;border-radius:50%;background:var(--orange)"></span>Lorem ipsum dolor sit amet, consectetur adipiscing elit. Aliquam odio nulla, blandit eu suscipit ac, pulvinar in mauris. Mauris ac sodales ante. Donec congue lectus vel libero facilisis luctus.</p>
    <p style="position:relative;margin-top:6px"><span style="position:absolute;left:-8px;top:1px;width:5px;height:5px;border-radius:50%;background:var(--orange)"></span>Lorem ipsum dolor sit amet, consectetur adipiscing elit. Aliquam odio nulla, blandit eu suscipit ac, pulvinar in mauris. Mauris ac sodales ante. Donec congue lectus vel libero facilisis luctus.</p>
  </div>
  <div class="footer"><span class="brand"><i></i>Quantiva</span><span class="rule"></span><span class="nav"><b>Next</b>Previous</span></div>
</section>

<section class="slide c3 r3">
  <div class="tile"></div>
  <div class="slide-title">Graphic Chart Style</div><div class="slide-sub">text for second title</div><div class="badge">9</div>
  <svg style="position:absolute;left:0;top:0" width="341" height="256" font-family="Open Sans, sans-serif" font-size="4.5" fill="#777">
    <g stroke="#e6e6e6" stroke-width=".5">
      <line x1="75" y1="70" x2="235" y2="70"/><line x1="75" y1="81" x2="235" y2="81"/><line x1="75" y1="93" x2="235" y2="93"/><line x1="75" y1="104" x2="235" y2="104"/><line x1="75" y1="116" x2="235" y2="116"/><line x1="75" y1="127" x2="235" y2="127"/><line x1="75" y1="138" x2="235" y2="138"/><line x1="75" y1="150" x2="235" y2="150"/><line x1="75" y1="161" x2="235" y2="161"/><line x1="75" y1="173" x2="235" y2="173"/>
    </g>
    <line x1="75" y1="184" x2="235" y2="184" stroke="#999" stroke-width=".6"/>
    <line x1="75" y1="66" x2="75" y2="196" stroke="#999" stroke-width=".6"/>
    <g text-anchor="end"><text x="72" y="72">10,000,000</text><text x="72" y="83">9,000,000</text><text x="72" y="95">8,000,000</text><text x="72" y="106">7,000,000</text><text x="72" y="118">6,000,000</text><text x="72" y="129">5,000,000</text><text x="72" y="140">4,000,000</text><text x="72" y="152">3,000,000</text><text x="72" y="163">2,000,000</text><text x="72" y="175">1,000,000</text><text x="72" y="198">(1,000,000)</text></g>
    <text x="40" y="130" transform="rotate(-90 40 130)">US $</text>
    <g text-anchor="middle"><text x="90" y="191">Year 1</text><text x="120" y="191">Year 2</text><text x="150" y="191">Year 3</text><text x="180" y="191">Year 4</text><text x="210" y="191">Year 5</text></g>
    <polyline points="90,176 120,169 150,152 180,118 210,85" fill="none" stroke="var(--orange)" stroke-width="1"/>
    <g fill="var(--orange)"><circle cx="90" cy="176" r="1.3"/><circle cx="120" cy="169" r="1.3"/><circle cx="150" cy="152" r="1.3"/><circle cx="180" cy="118" r="1.3"/><circle cx="210" cy="85" r="1.3"/></g>
    <polyline points="90,182 120,179 150,171 180,160 210,146" fill="none" stroke="#111" stroke-width="1"/>
    <g fill="#111"><rect x="89" y="181" width="2" height="2"/><rect x="119" y="178" width="2" height="2"/><rect x="149" y="170" width="2" height="2"/><rect x="179" y="159" width="2" height="2"/><rect x="209" y="145" width="2" height="2"/></g>
    <polyline points="90,184 120,183 150,182 180,176 210,171" fill="none" stroke="var(--yellow)" stroke-width="1"/>
    <g fill="var(--yellow)"><circle cx="90" cy="184" r="1.2"/><circle cx="120" cy="183" r="1.2"/><circle cx="150" cy="182" r="1.2"/><circle cx="180" cy="176" r="1.2"/><circle cx="210" cy="171" r="1.2"/></g>
    <g><line x1="245" y1="117" x2="255" y2="117" stroke="var(--orange)"/><text x="257" y="119">Total Revenue</text>
    <line x1="245" y1="126" x2="255" y2="126" stroke="#111"/><text x="257" y="128">Gross Profit</text>
    <line x1="245" y1="135" x2="255" y2="135" stroke="var(--yellow)"/><text x="257" y="137">Earning After Taxes (EAT)</text></g>
  </svg>
  <div class="footer"><span class="brand"><i></i>Quantiva</span><span class="rule"></span><span class="nav"><b>Next</b>Previous</span></div>
</section>

<section class="slide c1 r4">
  <div class="tile"></div>
  <div class="slide-title">Graphic Chart Style</div><div class="slide-sub">text for second title</div><div class="badge">10</div>
  <svg style="position:absolute;left:0;top:0" width="200" height="256" font-family="Open Sans, sans-serif" font-size="4" fill="#999">
    <g stroke="#eee" stroke-width=".5"><line x1="28" y1="70" x2="170" y2="70"/><line x1="28" y1="90" x2="170" y2="90"/><line x1="28" y1="110" x2="170" y2="110"/><line x1="28" y1="130" x2="170" y2="130"/><line x1="28" y1="150" x2="170" y2="150"/><line x1="28" y1="170" x2="170" y2="170"/></g>
    <line x1="28" y1="196" x2="170" y2="196" stroke="#ccc" stroke-width=".6"/>
    <g text-anchor="end"><text x="182" y="72">10</text><text x="182" y="85">09</text><text x="182" y="98">08</text><text x="182" y="112">07</text><text x="182" y="125">06</text><text x="182" y="138">05</text><text x="182" y="152">04</text><text x="182" y="165">03</text><text x="182" y="178">02</text><text x="182" y="191">01</text></g>
    <g fill="var(--gray)"><rect x="31" y="155" width="8" height="41"/><rect x="62" y="172" width="8" height="24"/><rect x="93" y="141" width="8" height="55"/><rect x="126" y="163" width="8" height="33"/></g>
    <g fill="var(--yellow)"><rect x="40" y="80" width="8" height="116"/><rect x="71" y="114" width="8" height="82"/><rect x="102" y="66" width="8" height="130"/><rect x="135" y="128" width="8" height="68"/></g>
    <g fill="var(--orange)"><rect x="49" y="114" width="8" height="82"/><rect x="80" y="126" width="8" height="70"/><rect x="111" y="104" width="8" height="92"/><rect x="144" y="172" width="8" height="24"/></g>
    <g fill="#777" font-size="5.5" text-anchor="middle"><text x="44" y="204">2009</text><text x="75" y="204">2010</text><text x="106" y="204">2011</text><text x="139" y="204">2012</text></g>
    <g font-size="3.6"><rect x="36" y="211" width="5" height="5" fill="var(--gray)"/><text x="43" y="214">Description</text><text x="43" y="219">short note here</text>
    <rect x="82" y="211" width="5" height="5" fill="var(--yellow)"/><text x="89" y="214">Description</text><text x="89" y="219">short note here</text>
    <rect x="126" y="211" width="5" height="5" fill="var(--orange)"/><text x="133" y="214">Description</text><text x="133" y="219">short note here</text></g>
  </svg>
  <div class="body" style="position:absolute;left:187px;top:62px;width:145px;display:grid;gap:11px">
    <p style="border-left:4px solid var(--gray);padding-left:8px">Lorem ipsum dolor sit amet, consectetur adipiscing elit. Aliquam odio nulla, blandit eu suscipit ac, pulvinar in mauris. Mauris ac sodales ante. Donec congue lectus vel libero facilisis luctus.</p>
    <p style="border-left:4px solid var(--yellow);padding-left:8px">Lorem ipsum dolor sit amet, consectetur adipiscing elit. Aliquam odio nulla, blandit eu suscipit ac, pulvinar in mauris. Mauris ac sodales ante. Donec congue lectus vel libero facilisis luctus.</p>
    <p style="border-left:4px solid var(--orange);padding-left:8px">Lorem ipsum dolor sit amet, consectetur adipiscing elit. Aliquam odio nulla, blandit eu suscipit ac, pulvinar in mauris. Mauris ac sodales ante. Donec congue lectus vel libero facilisis luctus.</p>
  </div>
  <div class="footer"><span class="brand"><i></i>Quantiva</span><span class="rule"></span><span class="nav"><b>Next</b>Previous</span></div>
</section>

<section class="slide c2 r4">
  <div class="tile"></div>
  <div class="slide-title">Timeline</div><div class="slide-sub">text for second title</div><div class="badge">11</div>
  <svg style="position:absolute;left:0;top:0" width="341" height="256" font-family="Open Sans, sans-serif" font-size="4" fill="#777">
    <line x1="14" y1="131" x2="330" y2="131" stroke="#999" stroke-width=".8"/>
    <g stroke="#888" stroke-width=".6" fill="none">
      <polyline points="27,131 27,77 47,77"/><polyline points="110,131 110,77 128,77"/><polyline points="191,131 191,77 209,77"/><polyline points="264,131 264,77 282,77"/>
      <polyline points="50,131 50,183 66,183"/><polyline points="133,131 133,183 150,183"/><polyline points="216,131 216,183 232,183"/><polyline points="284,131 284,183 300,183"/>
    </g>
    <g><circle cx="27" cy="131" r="2.5" fill="var(--orange)"/><circle cx="50" cy="131" r="2.5" fill="var(--orange)"/><circle cx="110" cy="131" r="2.5" fill="var(--yellow)"/><circle cx="133" cy="131" r="2.5" fill="var(--yellow)"/><circle cx="191" cy="131" r="2.5" fill="var(--gray)"/><circle cx="216" cy="131" r="2.5" fill="var(--gray)"/><circle cx="264" cy="131" r="2.5" fill="#111"/><circle cx="284" cy="131" r="2.5" fill="#111"/></g>
    <g font-size="8" text-anchor="middle" fill="#fff">
      <circle cx="27" cy="106" r="9" fill="var(--orange)"/><text x="27" y="109">A</text>
      <circle cx="110" cy="106" r="9" fill="var(--yellow)"/><text x="110" y="109">B</text>
      <circle cx="191" cy="106" r="9" fill="var(--gray)"/><text x="191" y="109">C</text>
      <circle cx="264" cy="106" r="9" fill="#111"/><text x="264" y="109">D</text>
      <circle cx="50" cy="154" r="9" fill="var(--orange)"/><text x="50" y="157">a</text>
      <circle cx="133" cy="154" r="9" fill="var(--yellow)"/><text x="133" y="157">b</text>
      <circle cx="216" cy="154" r="9" fill="var(--gray)"/><text x="216" y="157">c</text>
      <circle cx="284" cy="154" r="9" fill="#111"/><text x="284" y="157">d</text>
    </g>
    <g font-size="7.5"><text x="49" y="80" fill="var(--orange)">501</text><text x="130" y="80" fill="var(--yellow)">499</text><text x="211" y="80" fill="#333">385</text><text x="284" y="80" fill="#333">297</text>
    <text x="68" y="186" fill="var(--orange)">130</text><text x="152" y="186" fill="var(--yellow)">184</text><text x="234" y="186" fill="#333">319</text><text x="302" y="186" fill="#333">276</text></g>
    <text x="50" y="89">Content here,</text><text x="50" y="94">making it look</text><text x="50" y="99">like readable</text>
    <text x="131" y="89">Lorem Ipsum is</text><text x="131" y="94">that it has a</text><text x="131" y="99">more-or-less</text><text x="131" y="104">normal</text>
    <text x="212" y="89">Distribution of</text><text x="212" y="94">letters, as</text><text x="212" y="99">opposed to</text><text x="212" y="104">publishing</text>
    <text x="285" y="89">packages and</text><text x="285" y="94">you need to be</text><text x="285" y="99">sure there isn't</text><text x="285" y="104">anything</text>
    <text x="62" y="171">Lorem dolor,</text><text x="62" y="176">adipiscing</text>
    <text x="146" y="171">Established fact</text><text x="146" y="176">and web</text>
    <text x="229" y="171">Readable</text><text x="229" y="176">content</text>
    <text x="297" y="171">Consectetr</text><text x="297" y="176">adipiscing</text>
  </svg>
  <div class="footer"><span class="brand"><i></i>Quantiva</span><span class="rule"></span><span class="nav"><b>Next</b>Previous</span></div>
</section>

<section class="slide c3 r4 thanks">
  <h2>THANK YOU</h2>
  <div class="line"></div>
  <div class="contact" style="top:186px"><svg width="7" height="7" viewBox="0 0 10 10" fill="#fff"><path d="M2 0h2l1 3-1.5 1a6 6 0 0 0 2.5 2.5L7 5l3 1v2c0 1-1 2-2 2A8 8 0 0 1 0 2c0-1 1-2 2-2z"/></svg>000-000-0000</div>
  <div class="contact" style="top:202px"><svg width="7" height="6" viewBox="0 0 10 8" fill="#fff"><rect width="10" height="8" rx="1"/><path d="M0 0l5 4 5-4" stroke="var(--orange)" fill="none"/></svg>xyz@email.com</div>
  <div class="contact" style="top:218px"><svg width="7" height="7" viewBox="0 0 10 10" fill="none" stroke="#fff"><circle cx="5" cy="5" r="4.3"/><path d="M1 5h8M5 1c2 2 2 6 0 8M5 1c-2 2-2 6 0 8"/></svg>www.yourwebsite.com</div>
  <div class="line" style="top:232px"></div>
  <div class="social"><span></span><span></span><span></span></div>
</section>

</div>
</body>
</html>
```